Business card with branding treatment

I need to improve the stock logo created with the tool. Also I want a business card with typeface colors matching for modern upscale real estate agency. The clients are looking for upscale agency that is well established and professional. Palm Beach county is an upscale, luxury market. We handle new construction and mostly newer, modern homes. We offer internet marketing for home sellers and take advantage of social media. This logo will be on facebook and instagram channels as well as Youtube videos.

Target Market(s)

Home buyers and sellers nin Plam Beach Florida

Industry/Entity Type

Real Estate

Contact Information for Business Card

Logos name and contact info including youtube and facebook adresses

Font styles to use
Sans Serif

Requirements
Nice to have
• two versions one blue/white the other black/gold or black silver
Should not have
• scripted fonts

```html
<!DOCTYPE html>
<html lang="en">
<head>
<meta charset="utf-8">
<title>Harbor Key Estates – Business Card</title>
<link href="https://fonts.googleapis.com/css2?family=Arimo:wght@400;700&display=swap" rel="stylesheet">
<style>
  :root {
    --bg: #d9d9d9;
    --card-white: #f7f7f7;
    --brand-blue: #3fb0ee;
    --brand-blue-deep: #35a4ea;
    --text-gray: #6b6b6b;
    --text-dark: #3a3a3a;
    --divider: #9a9a9a;
    --broker-blue: #2a5c9c;
    --badge-black: #111111;
  }
  * { margin: 0; padding: 0; box-sizing: border-box; }
  html, body { width: 1200px; height: 1200px; overflow: hidden; }
  body {
    background: var(--bg);
    font-family: "Arimo", Arial, sans-serif;
    position: relative;
  }
  .card {
    position: absolute;
    left: 200px;
    width: 800px;
    height: 457px;
    border-radius: 24px;
  }
  .card-front { top: 110px; background: var(--card-white); }
  .card-back {
    top: 633px;
    background: linear-gradient(180deg, var(--brand-blue) 0%, var(--brand-blue-deep) 100%);
  }
  .brand-wordmark {
    position: absolute;
    white-space: nowrap;
    font-weight: 400;
    letter-spacing: -0.5px;
  }
  .card-front .brand-wordmark {
    left: 234px; top: 225px;
    transform: translate(-50%, -50%);
    font-size: 31px;
    color: var(--brand-blue);
  }
  .card-back .brand-wordmark {
    left: 400px; top: 228px;
    transform: translate(-50%, -50%);
    font-size: 50px;
    color: #ffffff;
  }
  .divider {
    position: absolute;
    left: 413px; top: 145px;
    width: 2px; height: 165px;
    background: linear-gradient(180deg, transparent, var(--divider) 20%, var(--divider) 80%, transparent);
  }
  .agent-name {
    position: absolute;
    left: 441px; top: 152px;
    font-size: 26px; font-weight: 700;
    color: var(--brand-blue);
    letter-spacing: 0.3px;
  }
  .agent-title {
    position: absolute;
    left: 441px; top: 184px;
    font-size: 18px;
    color: var(--text-gray);
  }
  .contact-list {
    position: absolute;
    left: 443px; top: 225px;
    list-style: none;
  }
  .contact-list li {
    display: flex; align-items: center;
    height: 23px;
    font-size: 18px;
    color: var(--text-dark);
  }
  .contact-list svg { width: 16px; height: 16px; margin-right: 12px; fill: var(--brand-blue); }
  .member-badge {
    position: absolute;
    left: 40px; top: 374px;
    width: 49px; height: 49px;
    background: var(--badge-black);
  }
  .broker-name {
    position: absolute;
    right: 42px; top: 398px;
    display: flex; align-items: center; gap: 8px;
    font-size: 20px;
    color: var(--broker-blue);
  }
  .broker-name .dot {
    width: 14px; height: 14px; border-radius: 50%;
    background: var(--broker-blue);
  }
</style>
</head>
<body>
  <section class="card card-front">
    <div class="brand-wordmark">HARBOR KEY ESTATES</div>
    <div class="divider"></div>
    <h1 class="agent-name">DANA WHITFIELD - PA</h1>
    <p class="agent-title">Managing Director</p>
    <ul class="contact-list">
      <li><svg viewBox="0 0 16 16"><path d="M3.5 1.5l2.5 0 1 3.5-1.6 1.2c.8 1.8 2.2 3.2 4 4l1.2-1.6 3.4 1v2.5c0 .8-.7 1.4-1.5 1.4C6.9 13.5 2.5 9.1 2.1 3c0-.8.6-1.5 1.4-1.5z"/></svg>555.014.2200</li>
      <li><svg viewBox="0 0 16 16"><path d="M1 3.5h14v9H1z M2 4.5v.3l6 4 6-4v-.3z" fill-rule="evenodd"/></svg>dana@harborkeyestates.com</li>
      <li><svg viewBox="0 0 16 16"><circle cx="8" cy="8" r="7"/><path d="M5 4c1.5 1 1 2.5 2.5 3s1 2-.5 3.5M10 3c-.5 1.5.5 2.5 2 2.5" stroke="#fff" stroke-width="1.2" fill="none"/></svg>www.harborkeyestates.com</li>
    </ul>
    <div class="member-badge" role="img" aria-label="Member association badge"></div>
    <div class="broker-name"><span class="dot"></span>summit brokers</div>
  </section>

  <section class="card card-back">
    <div class="brand-wordmark">HARBOR KEY ESTATES</div>
  </section>
</body>
</html>
```